To revamp/upgrade company website

We recently changed our company core values and mission statement, I have added this (very simply) via word press. However I would like the values and mission statement page design upgrading and also to have them run through the rest of the website pages. Also, open to other recommendations on how to update our website. The main take away from the website should be that we are the "people company", both for our customers and our staff. We would like the logo and colour theme to remain as is. Calderwick Healthcare is a health and social care company, who privately own a group of care homes in the north west of england. Attached is the core values, PEOPLE, our mission statement and also a word cloud that we would also like to embed in to the website.

```html
<!DOCTYPE html>
<html lang="en">
<head>
<meta charset="utf-8">
<title>Calderwick Healthcare – Caring For Your Life</title>
<link href="https://fonts.googleapis.com/css2?family=Outfit:wght@400;500;600&family=Questrial&display=swap" rel="stylesheet">
<style>
:root{
  --navy:#3b5573;
  --orange:#eea883;
  --ink:#2f3440;
  --muted:#4a4f5a;
  --hero-bg:#f5f7f9;
  --cream:#fdf6f2;
  --white:#ffffff;
  --card-shadow:0 2px 10px rgba(40,60,90,.10);
}
*{box-sizing:border-box;margin:0;padding:0}
html,body{width:1200px;height:3891px;overflow:hidden}
body{position:relative;background:var(--white);font-family:"Questrial",sans-serif;color:var(--ink)}
.abs{position:absolute}
.heading{font-family:"Outfit",sans-serif;font-weight:500;color:var(--navy);letter-spacing:-.5px;text-transform:uppercase}
.heading em{font-style:normal;color:var(--orange)}
.rule{position:absolute;height:3px;width:48px;background:var(--orange)}
.btn{position:absolute;display:flex;height:42px;text-decoration:none;font-family:"Outfit",sans-serif;font-size:14px;text-transform:uppercase;box-shadow:0 1px 4px rgba(0,0,0,.12)}
.btn .btn-icon{width:32px;background:var(--orange);display:flex;align-items:center;justify-content:center}
.btn .btn-label{flex:1;background:var(--navy);color:var(--white);display:flex;align-items:center;justify-content:center;padding:0 16px}
.btn.light .btn-label{background:var(--white);color:var(--navy)}
/* header */
.top-line{top:0;left:0;width:1200px;height:2px;background:var(--orange)}
.hero-bg{top:2px;left:0;width:1200px;height:500px}
.brand{top:37px;left:110px;display:flex;align-items:center;gap:10px}
.brand-mark{width:24px;height:24px;background:var(--navy)}
.brand-text{font-family:"Outfit",sans-serif;font-weight:500;color:var(--navy);font-size:28px;letter-spacing:.5px;line-height:1}
.main-nav{top:43px;left:410px;width:680px;display:flex;justify-content:space-between;font-family:"Outfit",sans-serif;font-size:14px;color:var(--ink)}
.main-nav a{color:inherit;text-decoration:none}
.main-nav a.active{color:var(--orange)}
.hero-title{top:164px;left:111px;font-size:34px}
.hero-sub{top:233px;left:111px;font-size:19px;color:var(--ink)}
/* values */
.values-title{top:553px;left:111px;font-size:34px}
.values-intro{top:640px;left:110px;width:430px;font-size:15.5px;line-height:35px;color:var(--ink)}
.value-card{position:absolute;width:233px;height:225px;background:var(--white);border-radius:12px;box-shadow:var(--card-shadow);padding:24px 24px 0 25px;overflow:hidden}
.value-card svg{display:block;width:58px;height:58px}
.value-card h3{font-family:"Outfit",sans-serif;font-weight:500;font-size:18px;color:var(--navy);margin-top:22px;letter-spacing:.3px}
.value-card p{font-size:14.5px;line-height:32px;color:var(--ink);margin-top:8px;height:64px;overflow:hidden}
.value-card.featured{background:var(--navy)}
.value-card.featured h3{color:var(--orange)}
.value-card.featured p{color:var(--white)}
/* about */
.about-band{top:1124px;left:0;width:1200px;height:754px;background:var(--navy)}
.about-title{top:1183px;left:111px;font-size:34px;color:var(--white);display:flex;align-items:center;gap:18px}
.about-title::after{content:"";width:48px;height:3px;background:var(--orange)}
.about-lead{top:1245px;left:111px;width:425px;font-family:"Outfit",sans-serif;font-size:15px;line-height:37px;color:var(--white);text-transform:uppercase}
.about-copy{top:1185px;left:657px;width:432px;font-size:15.5px;line-height:33.5px;color:var(--white)}
.photo{position:absolute;border-radius:10px}
/* care */
.care-title{top:1950px;left:0;width:1200px;text-align:center;font-size:34px}
.care-col{position:absolute;top:2061px;width:270px;text-align:center}
.care-icon{width:84px;height:84px;margin:0 auto;border-radius:50%;border:1px solid #e3e6ea;display:flex;align-items:center;justify-content:center;background:var(--white)}
.care-col h3{font-family:"Outfit",sans-serif;font-weight:500;font-size:18px;color:var(--navy);margin-top:38px;white-space:nowrap}
.care-col p{font-size:15.5px;line-height:32.5px;margin:14px auto 0;width:262px;color:var(--ink)}
/* news */
.news-title{top:2473px;left:0;width:1200px;text-align:center;font-size:34px}
.news-card{position:absolute;top:2575px;width:307px;height:372px;border-radius:12px;background:var(--white);box-shadow:var(--card-shadow);overflow:hidden}
.news-card .news-photo{height:184px;border-radius:12px 12px 0 0}
.news-body{padding:26px 26px 0 26px}
.news-date{display:flex;align-items:center;gap:12px;font-family:"Outfit",sans-serif;font-size:14px;color:var(--ink)}
.news-date i{display:inline-block;width:12px;height:10px;background:var(--orange);opacity:.6}
.news-body h3{font-family:"Outfit",sans-serif;font-weight:500;font-size:15px;color:var(--navy);margin-top:22px;text-transform:uppercase;white-space:nowrap}
.news-body p{font-size:15px;line-height:33px;margin-top:12px;height:66px;overflow:hidden}
.slider-arrow{position:absolute;top:2653px;width:28px;height:28px}
/* testimonial */
.reviews-band{top:3033px;left:0;width:1200px;height:495px;background:var(--cream)}
.reviews-title{top:3086px;left:0;width:1200px;text-align:center;font-size:34px}
.quote{top:3177px;left:165px;width:870px;text-align:center;font-size:15.5px;line-height:33.5px;color:var(--ink)}
.quote-author{top:3335px;left:0;width:1200px;text-align:center;font-family:"Outfit",sans-serif;font-size:19px;color:var(--navy);letter-spacing:-.3px}
/* footer */
.site-footer{top:3528px;left:0;width:1200px;height:363px;background:var(--navy);color:var(--white);font-family:"Outfit",sans-serif}
.footer-brand{position:absolute;top:72px;left:0;width:1200px;text-align:center;font-size:28px;font-weight:500;letter-spacing:1px}
.footer-contact{position:absolute;top:174px;font-size:13.5px;display:flex;align-items:center;gap:12px;text-transform:uppercase;white-space:nowrap}
.footer-divider{position:absolute;top:221px;left:111px;width:978px;height:1px;background:rgba(255,255,255,.18)}
.footer-nav{position:absolute;top:247px;left:160px;display:flex;font-size:14px;text-transform:uppercase}
.footer-nav span.sep{margin:0 33px}
.copyright{position:absolute;top:318px;left:0;width:1200px;text-align:center;font-size:13px;text-transform:uppercase}
</style>
</head>
<body>

<div class="abs top-line"></div>
<svg class="abs hero-bg" viewBox="0 0 1200 500" preserveAspectRatio="none" aria-hidden="true">
  <path d="M0 0H1200V330C1120 360 960 420 780 470C640 505 520 470 360 420C200 370 80 360 0 345Z" fill="var(--hero-bg)"/>
</svg>

<header>
  <div class="abs brand">
    <span class="brand-mark"></span>
    <span class="brand-text">CALDERWICK</span>
  </div>
  <nav class="abs main-nav">
    <a class="active" href="#">HOME</a>
    <a href="#">ABOUT US</a>
    <a href="#">LIVE WITH US</a>
    <a href="#">HOW WE CARE</a>
    <a href="#">HELP &amp; SUPPORT</a>
    <a href="#">WORK WITH US</a>
  </nav>
</header>

<section class="hero">
  <h1 class="abs heading hero-title">Caring for <em>your life</em></h1>
  <p class="abs hero-sub">In a safe, secure and welcoming environment</p>
  <a class="btn" href="#" style="top:299px;left:112px;width:164px">
    <span class="btn-icon"><svg width="12" height="12" viewBox="0 0 12 12"><path d="M2 10L10 2M4 2h6v6" stroke="#fff" stroke-width="1.3" fill="none"/></svg></span>
    <span class="btn-label">Get in touch</span>
  </a>
</section>

<section class="values">
  <h2 class="abs heading values-title">Our core <em>values</em></h2>
  <div class="rule" style="top:611px;left:111px"></div>
  <p class="abs values-intro">We are introducing a new set of values that reflect our shared priorities and define how we show up for each other every day:</p>

  <div class="value-card" style="top:564px;left:607px">
    <svg viewBox="0 0 58 58" fill="none" stroke="var(--navy)" stroke-width="2"><circle cx="29" cy="29" r="20"/><circle cx="29" cy="29" r="14"/><path d="M29 3v8M29 47v8M3 29h8M47 29h8"/><path d="M22 29l5 5 10-10" stroke="var(--orange)" stroke-width="3"/></svg>
    <h3>PURPOSE</h3>
    <p>We are driven by a clear understanding of why we</p>
  </div>
  <div class="value-card" style="top:564px;left:855px">
    <svg viewBox="0 0 58 58" fill="none" stroke="var(--navy)" stroke-width="2"><path d="M29 6l5 10 11 1-8 8 2 11-10-6-10 6 2-11-8-8 11-1z" fill="var(--orange)" stroke="none"/><path d="M10 46c6-4 12-4 18 0h12c3 0 3 4 0 4H26M4 10l6 4M54 10l-6 4M4 24h6M54 24h-6"/></svg>
    <h3>EXCELLENCE</h3>
    <p>We hold ourselves to the highest standards</p>
  </div>
  <div class="value-card" style="top:813px;left:112px">
    <svg viewBox="0 0 58 58" fill="none" stroke="var(--navy)" stroke-width="2"><path d="M4 12h22c2 0 3 2 3 4v32c0-2-1-3-3-3H4zM54 12H32c-2 0-3 2-3 4v32c0-2 1-3 3-3h22z" fill="var(--orange)" fill-opacity=".55"/><path d="M9 20h14M9 26h14M9 32h14M35 20h14M35 26h14M35 32h14"/></svg>
    <h3>OPENNESS</h3>
    <p>We build trust through honest, respectful</p>
  </div>
  <div class="value-card featured" style="top:813px;left:360px">
    <svg viewBox="0 0 58 58" fill="none" stroke="var(--white)" stroke-width="2"><path d="M29 10a13 13 0 0 0-8 23c2 2 3 4 3 7h10c0-3 1-5 3-7a13 13 0 0 0-8-23z"/><path d="M29 18l3 5-3 5-3-5z" fill="var(--orange)" stroke="none"/><path d="M24 44h10M25 48h8M29 2v4M10 10l3 3M48 10l-3 3M4 25h4M50 25h4"/></svg>
    <h3>PASSION</h3>
    <p>We are passionate about delivering exceptional care</p>
  </div>
  <div class="value-card" style="top:813px;left:607px">
    <svg viewBox="0 0 58 58" fill="none" stroke="var(--navy)" stroke-width="2"><circle cx="29" cy="29" r="24"/><circle cx="29" cy="29" r="9" fill="var(--orange)" stroke="none"/><circle cx="29" cy="29" r="14" stroke-dasharray="4 3"/><circle cx="29" cy="29" r="3" fill="var(--white)" stroke="none"/></svg>
    <h3>LEARNING</h3>
    <p>We are committed to personal and professional</p>
  </div>
  <div class="value-card" style="top:813px;left:855px">
    <svg viewBox="0 0 58 58" fill="none" stroke="var(--navy)" stroke-width="2"><path d="M16 52V40c-6-4-9-10-8-18C10 10 20 4 30 6c10 2 15 10 14 18l4 8h-5v8c0 3-2 4-5 4h-6v8"/><path d="M30 14c3-4 9-3 9 2 0 4-9 10-9 10s-9-6-9-10c0-5 6-6 9-2z" fill="var(--orange)" stroke="none"/></svg>
    <h3>EMPATHY</h3>
    <p>We actively listen and seek to understand</p>
  </div>
</section>

<section class="abs about-band"></section>
<h2 class="abs heading about-title">About <em>us</em></h2>
<p class="abs about-lead">A home from home with Calderwick. Every resident is someone's family, and they deserve to feel respected, safe and at home.</p>
<p class="abs about-copy">Our daily mission is to make each moment meaningful for us and for those around us through acts of kindness, integrity, and connection. We provide compassionate, person-centred care that honours the lives and legacies of our residents and their families, while fostering a culture where our staff feel empowered, valued, and inspired to grow.</p>
<a class="btn light" href="#" style="top:1448px;left:657px;width:164px">
  <span class="btn-icon"><svg width="12" height="12" viewBox="0 0 12 12"><path d="M2 10L10 2M4 2h6v6" stroke="#fff" stroke-width="1.3" fill="none"/></svg></span>
  <span class="btn-label">Learn more</span>
</a>
<div class="photo" role="img" aria-label="Care worker chatting with residents in a bright lounge" style="top:1389px;left:112px;width:475px;height:298px;background:linear-gradient(135deg,#e8e1d6,#b9b2a6 55%,#7e8a94)"></div>
<div class="photo" role="img" aria-label="Nursing staff in blue uniforms helping an elderly resident walk" style="top:1534px;left:541px;width:548px;height:261px;background:linear-gradient(120deg,#d9c7a8,#c7b08e 40%,#6d8fb5 75%,#4f75a3);border:3px solid var(--navy)"></div>

<section class="care">
  <h2 class="abs heading care-title">How we <em>care</em></h2>
  <div class="rule" style="top:2009px;left:576px"></div>
  <div class="care-col" style="left:102px">
    <div class="care-icon"><svg width="46" height="46" viewBox="0 0 46 46" fill="none" stroke="var(--navy)" stroke-width="1.8"><path d="M14 12h18v6H14z" fill="var(--orange)" stroke="none"/><circle cx="23" cy="22" r="8"/><path d="M8 44c0-9 6-13 15-13s15 4 15 13M20 36h6"/></svg></div>
    <h3>GENERAL NURSING CARE</h3>
    <p>We offer general nursing care for those living with long term illnesses and those who need complex</p>
  </div>
  <div class="care-col" style="left:463px">
    <div class="care-icon"><svg width="46" height="46" viewBox="0 0 46 46" fill="none" stroke="var(--navy)" stroke-width="1.8"><path d="M12 42V33c-5-3-7-8-6-14C8 9 16 4 24 5c9 1 14 8 13 15l3 6h-4v6c0 2-1 3-4 3h-4v7"/><circle cx="30" cy="12" r="6" fill="var(--orange)" stroke="none"/><path d="M27 12l2 2 4-4" stroke="var(--white)"/></svg></div>
    <h3>MENTAL HEALTH NURSING</h3>
    <p>We are able to offer a wide range of specialist nursing care for those who have experienced long term health</p>
  </div>
  <div class="care-col" style="left:823px">
    <div class="care-icon"><svg width="46" height="46" viewBox="0 0 46 46" fill="none" stroke="var(--navy)" stroke-width="1.8"><path d="M23 20c2-4 8-4 8 1 0 4-8 9-8 9s-8-5-8-9c0-5 6-5 8-1z" fill="var(--orange)" stroke="none"/><path d="M4 18l4 14 8 6v6M42 18l-4 14-8 6v6M8 14l4 12M38 14l-4 12"/></svg></div>
    <h3>RESIDENTIAL CARE</h3>
    <p>Our compassionate care team can provide you with companionship and support in our residential care</p>
  </div>
  <a class="btn" href="#" style="top:2356px;left:505px;width:189px">
    <span class="btn-icon"><svg width="12" height="12" viewBox="0 0 12 12"><path d="M2 10L10 2M4 2h6v6" stroke="#fff" stroke-width="1.3" fill="none"/></svg></span>
    <span class="btn-label">View more care</span>
  </a>
</section>

<section class="news">
  <h2 class="abs heading news-title">Latest news &amp; <em>blog</em></h2>
  <div class="rule" style="top:2526px;left:576px"></div>
  <svg class="slider-arrow" style="left:38px" viewBox="0 0 28 28" fill="none" stroke="var(--ink)" stroke-width="1.5"><circle cx="14" cy="14" r="12.5"/><path d="M20 14H8M12 10l-4 4 4 4"/></svg>
  <svg class="slider-arrow" style="left:1127px" viewBox="0 0 28 28" fill="none" stroke="var(--ink)" stroke-width="1.5"><circle cx="14" cy="14" r="12.5"/><path d="M8 14h12M16 10l4 4-4 4"/></svg>

  <article class="news-card" style="left:112px">
    <div class="news-photo" role="img" aria-label="Family members sitting together at a table" style="background:linear-gradient(120deg,#3a3f4a,#c9b7a2 45%,#e9e4dc)"></div>
    <div class="news-body">
      <div class="news-date"><i></i>JULY 2, 2025</div>
      <h3>A Joyous June!</h3>
      <p>Another month has come to an end and we've been reminiscing about</p>
    </div>
  </article>
  <article class="news-card" style="left:446px">
    <div class="news-photo" role="img" aria-label="Smiling carer talking with an older man" style="background:linear-gradient(120deg,#8a6248,#c79d7a 45%,#6b5447)"></div>
    <div class="news-body">
      <div class="news-date"><i></i>APRIL 23, 2025</div>
      <h3>Elm Lodge open day 30th April</h3>
      <p>In exciting news, Elm Lodge are preparing to open their brand new</p>
    </div>
  </article>
  <article class="news-card" style="left:781px">
    <div class="news-photo" role="img" aria-label="Residents and carer enjoying a table game together" style="background:linear-gradient(120deg,#a9c2a4,#d8d2c8 45%,#8b93a8)"></div>
    <div class="news-body">
      <div class="news-date"><i></i>FEBRUARY 20, 2024</div>
      <h3>Calderwick Valentines</h3>
      <p>This year Calderwick Healthcare celebrated Valentines Day with the</p>
    </div>
  </article>
</section>

<section class="abs reviews-band"></section>
<h2 class="abs heading reviews-title">What our families <em>say...</em></h2>
<div class="rule" style="top:3145px;left:576px"></div>
<p class="abs quote">I wish to commend the Activities Co-ordinator for his caring, dedicated manner. He organises many events to enrich the lives of the residents, such as the cinema club and regular live music performances. The particular act I wish to commend the activities coordinator for is when he took my mother and father's wedding photo away to mend the frame. This was a kind and generous act which is typical of him.</p>
<p class="abs quote-author">JR - SON OF RESIDENT</p>
<a class="btn" href="#" style="top:3401px;left:493px;width:214px">
  <span class="btn-icon"><svg width="12" height="12" viewBox="0 0 12 12"><path d="M2 10L10 2M4 2h6v6" stroke="#fff" stroke-width="1.3" fill="none"/></svg></span>
  <span class="btn-label">View more reviews</span>
</a>

<footer class="abs site-footer">
  <div class="footer-brand">CALDERWICK</div>
  <div class="footer-contact" style="left:137px">
    <svg width="14" height="14" viewBox="0 0 14 14"><path d="M3 1l2.5 3-1.5 1.5c1 2 2.5 3.5 4.5 4.5L10 8.5l3 2.5-1.5 2C6 13 1 8 1 2.5z" fill="#fff"/></svg>
    01632 960418
  </div>
  <div class="footer-contact" style="left:392px">
    <svg width="12" height="15" viewBox="0 0 12 15"><path d="M6 0a6 6 0 0 1 6 6c0 4-6 9-6 9S0 10 0 6a6 6 0 0 1 6-6z" fill="#fff"/><circle cx="6" cy="6" r="2.2" fill="var(--navy)"/></svg>
    Ground Floor, Unit 4, Harrow Court, Harrow Way, Millbrook, Lancs, PR9 1ZZ
  </div>
  <div class="footer-divider"></div>
  <nav class="footer-nav">
    <span>Home</span><span class="sep">|</span><span>About us</span><span class="sep">|</span><span>Live with us</span><span class="sep">|</span><span>How we care</span><span class="sep">|</span><span>Help &amp; support</span><span class="sep">|</span><span>Work with us</span>
  </nav>
  <p class="copyright">©2025 Calderwick Healthcare copyrights - all rights reserved</p>
</footer>

</body>
</html>
```